Need a design for Loan Site with new age design

We need a design for our site www.credvista.in , we deal with different verticals like home loan, personal loan, loan against property and business loans. Feel free to get in touch if you have any questions.

I have like the concept of the drop down on the eye level where consumer is able to select the product they wish and continue with the form https://www.tulsiorbit.com/ . They are in the same line of business as we are.

Here are few more designs which i personally like just to get idea about the taste

https://plumridgestudio.com/
http://zenpik.com/partners

Industry/Entity Type

Loan

Number of Pages Required

2 page

Colors
34a7d7
add136
faa54b
fbee3e

Requirements
Must have
• I have like the concept of the drop down on the eye level where consumer is able to select the product they wish and continue with the form https://www.tulsiorbit.com/ . They are in the same line of business as we are.
• Here are few more designs which i personally like just to get idea about the taste
• https://plumridgestudio.com/
• http://zenpik.com/partners

```html
<!DOCTYPE html>
<html lang="en">
<head>
<meta charset="utf-8">
<title>CredVista — Secured and Unsecured Loans</title>
<link href="https://fonts.googleapis.com/css2?family=Cabin:wght@400;500;600&family=Lato:wght@400;700&family=Open+Sans:wght@400;600;700&display=swap" rel="stylesheet">
<style>
:root{
  --blue:#34a7d7;
  --topbar:#3aa9dc;
  --navy:#323f52;
  --green:#add136;
  --mustard:#d6c237;
  --orange:#faa54b;
  --yellow:#fbee3e;
  --grey-bg:#e7e7e7;
  --field:#7d8590;
  --text:#6a6a6a;
  --white:#ffffff;
}
*{box-sizing:border-box;margin:0;padding:0}
html,body{width:784px;height:1200px;overflow:hidden;background:var(--white)}
body{position:relative;font-family:"Lato",sans-serif;color:var(--text)}

.topbar{position:absolute;top:0;left:0;width:784px;height:28px;background:var(--topbar);
  display:flex;justify-content:flex-end;align-items:center;gap:18px;padding-right:62px;
  font-family:"Open Sans",sans-serif;font-size:8.5px;font-weight:700;color:var(--white)}
.topbar-item{display:flex;align-items:center;gap:5px}
.topbar-item svg{width:10px;height:10px}

.site-header{position:absolute;top:28px;left:0;width:784px;height:61px;background:var(--white)}
.brand{position:absolute;left:64px;top:14px;display:flex;align-items:center;gap:6px;
  font-family:"Cabin",sans-serif;font-weight:500;font-size:17px;color:var(--blue)}
.brand-mark{width:16px;height:16px;background:var(--blue)}
.main-nav{position:absolute;right:62px;top:24px;display:flex;
  font-family:"Open Sans",sans-serif;font-size:8.5px;font-weight:700;color:var(--blue)}
.main-nav a{color:inherit;text-decoration:none;padding-bottom:6px;margin-left:36px}
.main-nav a.active{color:var(--green);border-bottom:2px solid var(--blue)}

.hero{position:absolute;top:89px;left:0;width:784px;height:378px;background:var(--navy);overflow:hidden}
.hero-title{position:absolute;left:64px;top:90px;font-family:"Cabin",sans-serif;font-weight:500;font-size:21px;color:var(--blue)}
.hero-sub{position:absolute;left:64px;top:121px;font-family:"Cabin",sans-serif;font-size:14px;color:var(--blue)}
.select{position:absolute;left:65px;width:366px;height:29px;background:var(--field);color:var(--white);
  font-family:"Open Sans",sans-serif;font-size:12px;display:flex;align-items:center;justify-content:space-between;padding:0 10px 0 8px}
.select svg{width:9px;height:6px}
.select-purpose{top:159px}
.select-product{top:199px}
.search-btn{position:absolute;left:65px;top:249px;height:31px;display:flex}
.search-btn .label{width:63px;background:var(--green);color:var(--navy);font-family:"Open Sans",sans-serif;font-weight:700;font-size:10.5px;display:flex;align-items:center;justify-content:center}
.search-btn .icon{width:31px;background:var(--mustard);display:flex;align-items:center;justify-content:center}
.art{position:absolute}
.art-desk{right:0;top:80px;width:390px;height:298px;background:linear-gradient(135deg,#5a4636 0%,#f3f1ea 45%,#d8b86a 75%,var(--navy) 100%);opacity:.9;border-radius:4px 0 0 0}
.art-clips{left:0;top:0;width:104px;height:64px;background:linear-gradient(135deg,#f2e56a,#f0f0f0);opacity:.55}
.art-glasses{right:0;top:0;width:104px;height:56px;background:linear-gradient(135deg,#e9eef0,#5fc2c7);opacity:.6}
.art-pencils{left:0;top:270px;width:96px;height:108px;background:linear-gradient(45deg,#f3ec3a,#3fc78e,#f3f3f3);opacity:.6}

.partners{position:absolute;top:467px;left:0;width:784px;height:270px;background:var(--white)}
.art-handshake{left:120px;top:29px;width:200px;height:208px;border-radius:50%;background:radial-gradient(circle,#3a5aa0 0%,#3aa5d8 60%,#3aa5d8 100%)}
.section-title{font-family:"Cabin",sans-serif;font-weight:500;font-size:14.5px;color:var(--blue);letter-spacing:.3px;line-height:1.3}
.partners .section-title{position:absolute;left:401px;top:29px;width:330px}
.rule{width:34px;height:4px;background:var(--green)}
.partners .rule{position:absolute;left:401px;top:70px}
.partners p{position:absolute;left:400px;top:104px;width:325px;font-size:8.3px;line-height:1.55}
.bank-grid{position:absolute;left:401px;top:160px;width:322px;display:grid;grid-template-columns:repeat(3,1fr);row-gap:26px}
.bank{font-family:"Lato",sans-serif;font-weight:700;font-size:10.5px;color:var(--navy);display:flex;align-items:center;gap:5px;height:20px;white-space:nowrap}
.bank:nth-child(3n){justify-content:flex-end}
.bank:nth-child(3n+2){justify-content:center}
.bank i{width:9px;height:9px;background:var(--navy);display:block}

.features{position:absolute;top:737px;left:0;width:784px;height:241px;background:var(--grey-bg);text-align:center}
.features .section-title{position:absolute;left:0;width:784px;top:29px}
.features .rule{position:absolute;left:375px;top:52px}
.features p{position:absolute;left:98px;top:82px;width:588px;font-size:8.3px;line-height:1.65}
.feature{position:absolute;top:142px;width:130px;margin-left:-65px;font-family:"Open Sans",sans-serif;font-size:10px;line-height:1.5;color:#666}
.feature svg{width:32px;height:32px;display:block;margin:0 auto 10px}

.cta{position:absolute;top:978px;left:0;width:784px;height:180px;background:var(--navy)}
.art-chat{left:64px;top:14px;width:164px;height:160px;border-radius:50%;background:radial-gradient(circle,#f2f2f2 0%,#b9d133 45%,#2f9b4a 75%,var(--navy) 100%);opacity:.85}
.cta .section-title{position:absolute;left:290px;width:444px;text-align:center;top:30px}
.cta p{position:absolute;left:285px;width:450px;top:62px;text-align:center;font-size:8.3px;line-height:1.6;color:#e4e7ec}
.inquire-btn{position:absolute;left:458px;top:113px;width:94px;height:32px;background:var(--green);color:var(--navy);
  font-family:"Open Sans",sans-serif;font-weight:700;font-size:10.5px;display:flex;align-items:center;justify-content:center}

.site-footer{position:absolute;top:1158px;left:0;width:784px;height:42px;background:var(--white);border-bottom:1px solid #cfcfcf;
  display:flex;align-items:center;justify-content:center;gap:8px;font-family:"Open Sans",sans-serif;font-size:8.5px;color:#444}
.site-footer .sep{width:1px;height:12px;background:#444}
</style>
</head>
<body>

<div class="topbar">
  <span class="topbar-item"><svg viewBox="0 0 10 10"><circle cx="5" cy="5" r="4.3" fill="none" stroke="#fff" stroke-width="1"/><path d="M3.4 3h1l.5 1.2-.6.5a3 3 0 0 0 1.1 1.1l.5-.6 1.2.5v1A3.6 3.6 0 0 1 3.4 3z" fill="#fff"/></svg>Call : 98765 43210</span>
  <span class="topbar-item"><svg viewBox="0 0 10 10"><circle cx="5" cy="5" r="4.3" fill="none" stroke="#fff" stroke-width="1"/><circle cx="5" cy="4" r="1.4" fill="#fff"/><path d="M2.6 7.6a2.6 2.6 0 0 1 4.8 0z" fill="#fff"/></svg>Login</span>
  <span class="topbar-item"><svg viewBox="0 0 10 10"><circle cx="5" cy="5" r="4.3" fill="none" stroke="#fff" stroke-width="1"/><path d="M3 5h4M5 3l2 2-2 2" fill="none" stroke="#fff" stroke-width="1"/></svg>Register</span>
</div>

<header class="site-header">
  <div class="brand"><span class="brand-mark"></span>CredVista</div>
  <nav class="main-nav">
    <a class="active">HOME</a><a>ABOUT</a><a>FEATURES</a><a>FAQ</a><a>PARTNERS</a><a>CONTACT</a>
  </nav>
</header>

<section class="hero">
  <div class="art art-clips" role="img" aria-label="Scattered paper clips"></div>
  <div class="art art-glasses" role="img" aria-label="Reading glasses on the desk"></div>
  <div class="art art-pencils" role="img" aria-label="Coloured pencils"></div>
  <div class="art art-desk" role="img" aria-label="Desk scene with clipboard of notes, ruler, pen and a cup of coffee"></div>

  <h1 class="hero-title">Looking For a Secured Or Unsecured Loan ?</h1>
  <div class="hero-sub">We will help you get Best Interest Rate</div>

  <div class="select select-purpose">I would like to <svg viewBox="0 0 9 6"><path d="M.5.5 4.5 5 8.5.5" fill="none" stroke="#fff"/></svg></div>
  <div class="select select-product">Select a product <svg viewBox="0 0 9 6"><path d="M.5.5 4.5 5 8.5.5" fill="none" stroke="#fff"/></svg></div>
  <div class="search-btn"><span class="label">Search</span><span class="icon"><svg width="12" height="12" viewBox="0 0 12 12"><circle cx="5" cy="5" r="3.6" fill="none" stroke="#fff" stroke-width="1.8"/><path d="M7.6 7.6 11 11" stroke="#fff" stroke-width="2"/></svg></span></div>
</section>

<section class="partners">
  <div class="art art-handshake" role="img" aria-label="Two businessmen shaking hands in front of a blue circle"></div>
  <h2 class="section-title">WE WORK WITH ALL PREMIUM FINANCIAL INSTITUTIONS</h2>
  <div class="rule"></div>
  <p>Lorem ipsum dolor sit amet, consectetuer adipiscing elit, sed quis Lorem ipsum dolor sit amet, consectetuer adipiscing elit, sed quisnostrud exerci tation ullamc orper suscipitnostrud exerci tation ullamcorper suscipit.</p>
  <div class="bank-grid">
    <div class="bank">Halvorne Bank</div>
    <div class="bank"><i></i>Quintara Bank</div>
    <div class="bank">Solvika Finance</div>
    <div class="bank"><i></i>Kestovel Bank</div>
    <div class="bank">Varunex Finserv</div>
    <div class="bank">Orvaline Bank</div>
  </div>
</section>

<section class="features">
  <h2 class="section-title">FEATURES</h2>
  <div class="rule"></div>
  <p>Lorem ipsum dolor sit amet, consectetuer adipiscing elit, sed quis Lorem ipsum dolor sit amet, consectetuer adipiscing elit, sed quisnostrud exerci tation ullamcorper suscipitnostrud exerci tation ullamcorper suscipit.</p>

  <div class="feature" style="left:141px">
    <svg viewBox="0 0 32 32"><rect x="4" y="6" width="24" height="22" fill="none" stroke="#34a7d7" stroke-width="2"/><rect x="4" y="6" width="24" height="5" fill="#34a7d7"/><path d="M10 3v6M22 3v6" stroke="#34a7d7" stroke-width="2"/><path d="M11 19l4 4 7-8" fill="none" stroke="#add136" stroke-width="2.4"/></svg>
    Get Approval within 7<br>business days
  </div>
  <div class="feature" style="left:307px">
    <svg viewBox="0 0 32 32"><circle cx="9" cy="9" r="4" fill="#34a7d7"/><circle cx="23" cy="9" r="4" fill="#34a7d7"/><path d="M2 28v-8a6 6 0 0 1 12 0v8zM18 28v-8a6 6 0 0 1 12 0v8z" fill="#34a7d7"/><rect x="12" y="19" width="8" height="6" fill="#add136"/></svg>
    Doorstep Deliveries
  </div>
  <div class="feature" style="left:477px">
    <svg viewBox="0 0 32 32"><path d="M5 5h16l3 3v20H5z" fill="#34a7d7"/><path d="M10 3h18v21H10z" fill="#fff" stroke="#34a7d7" stroke-width="2"/><path d="M14 9h10M14 13h10M14 17h7" stroke="#add136" stroke-width="1.6"/></svg>
    Easy Documentation
  </div>
  <div class="feature" style="left:645px;width:150px;margin-left:-75px">
    <svg viewBox="0 0 32 32"><path d="M16 2 30 9H2z" fill="#34a7d7"/><rect x="4" y="11" width="24" height="15" fill="none" stroke="#34a7d7" stroke-width="2"/><rect x="2" y="27" width="28" height="3" fill="#34a7d7"/><circle cx="16" cy="18.5" r="4.5" fill="#add136"/></svg>
    Compare Quote from all major<br>financial institutions
  </div>
</section>

<section class="cta">
  <div class="art art-chat" role="img" aria-label="Speech bubbles with question and idea icons circled by green arrows"></div>
  <h2 class="section-title">WHAT ARE YOU WAITING FOR?</h2>
  <p>Lorem ipsum dolor sit amet, consectetuer adipiscing elit, sed quis Lorem ipsum dolor sit amet, consectetuer adipiscing elit, sed quisnostrud exerci tation ullamcorper suscipitnostrud .</p>
  <div class="inquire-btn">Inquire Now</div>
</section>

<footer class="site-footer">
  <span>Privacy Policy</span><span class="sep"></span><span>Copyright © 2016 CredVista</span>
</footer>

</body>
</html>
```